kestrova business cards

Hey design gurus!
I'm after a clean, modern, stylish business card for my about to be launched company.
I've uploaded the logos for my company "Kestrova Electrical Solutions"
and also the tarrow alliance logo to whom i am associated.

```html
<!DOCTYPE html>
<html lang="en">
<head>
<meta charset="utf-8">
<title>Kestrova Electrical Solutions – Business Cards</title>
<link rel="stylesheet" href="https://fonts.googleapis.com/css2?family=Michroma&family=Poppins:wght@400;500&display=swap">
<style>
  :root {
    --page: #2b2b2d;
    --card: #0b1821;
    --card-edge: #11222d;
    --brand-blue: #1f8fd6;
    --white: #f2f5f7;
    --muted: #c9d2d8;
    --ghost: #1a2933;
  }
  * { box-sizing: border-box; margin: 0; padding: 0; }
  html, body { width: 1200px; height: 880px; overflow: hidden; }
  body {
    background: var(--page);
    display: flex;
    flex-direction: column;
    align-items: center;
    justify-content: center;
    gap: 40px;
  }
  .card {
    position: relative;
    width: 660px;
    height: 377px;
    border-radius: 18px;
    background: linear-gradient(135deg, var(--card-edge), var(--card) 55%);
    overflow: hidden;
    color: var(--white);
    font-family: "Poppins", sans-serif;
  }
  .ghost-ring {
    position: absolute;
    width: 300px; height: 300px;
    right: 40px; top: -40px;
    border-radius: 50%;
    border: 14px solid var(--ghost);
  }
  .brand {
    position: absolute;
    display: flex;
    align-items: center;
    gap: 16px;
  }
  .brand-dot {
    width: 62px; height: 62px;
    border-radius: 50%;
    background: var(--brand-blue);
    flex: none;
  }
  .brand-name {
    font-family: "Michroma", sans-serif;
    color: var(--brand-blue);
    line-height: 1.25;
  }
  .brand-name .main { display: block; font-size: 30px; letter-spacing: 1px; }
  .brand-name .sub { display: block; font-size: 11.5px; letter-spacing: 2.4px; }
  .card--front .brand { left: 118px; top: 146px; }
  .card--front .website {
    position: absolute;
    left: 0; right: 0; bottom: 44px;
    text-align: center;
    font-size: 15px;
    color: var(--white);
    letter-spacing: 0.4px;
  }
  .card--back .brand { left: 40px; top: 40px; }
  .card--back .brand-dot { width: 56px; height: 56px; }
  .person {
    position: absolute;
    left: 44px; top: 148px;
  }
  .person-name {
    font-family: "Michroma", sans-serif;
    color: var(--brand-blue);
    font-size: 21px;
    letter-spacing: 1px;
  }
  .person-role {
    font-family: "Michroma", sans-serif;
    color: var(--white);
    font-size: 12.5px;
    letter-spacing: 1.6px;
    margin-top: 2px;
  }
  .contact-list {
    list-style: none;
    margin-top: 16px;
    font-size: 14px;
    line-height: 1.5;
  }
  .contact-list li { display: flex; align-items: center; gap: 10px; }
  .contact-list svg { width: 13px; height: 13px; fill: var(--brand-blue); flex: none; }
  .address {
    margin-top: 14px;
    font-size: 14px;
    line-height: 1.35;
    color: var(--white);
    font-style: normal;
  }
  .partner-badge {
    position: absolute;
    right: 40px; bottom: 52px;
    width: 160px; height: 50px;
    border: 1.5px solid var(--muted);
    border-radius: 4px;
    display: flex;
    align-items: center;
    padding-left: 10px;
  }
  .partner-badge span {
    width: 30px; height: 30px;
    background: var(--white);
    border-radius: 2px;
  }
</style>
</head>
<body>

  <section class="card card--front" aria-label="Business card front">
    <div class="ghost-ring" aria-hidden="true"></div>
    <div class="brand">
      <div class="brand-dot" aria-hidden="true"></div>
      <div class="brand-name">
        <span class="main">KESTROVA</span>
        <span class="sub">ELECTRICAL SOLUTIONS</span>
      </div>
    </div>
    <p class="website">www.kestrovaelectric.com</p>
  </section>

  <section class="card card--back" aria-label="Business card back">
    <div class="ghost-ring" aria-hidden="true"></div>
    <div class="brand">
      <div class="brand-dot" aria-hidden="true"></div>
      <div class="brand-name">
        <span class="main">KESTROVA</span>
        <span class="sub">ELECTRICAL SOLUTIONS</span>
      </div>
    </div>

    <div class="person">
      <h1 class="person-name">DANIEL HARROW</h1>
      <p class="person-role">MANAGING DIRECTOR</p>
      <ul class="contact-list">
        <li>
          <svg viewBox="0 0 16 16" aria-hidden="true"><path d="M3.6 1.5l2.3 2.6-1.3 1.7c.9 2 2.5 3.6 4.6 4.6l1.7-1.3 2.6 2.3-1.2 2.3C7.5 15.4.6 8.5.9 2.7z"/></svg>
          214-555-0148
        </li>
        <li>
          <svg viewBox="0 0 16 16" aria-hidden="true"><path d="M1 3h14v10H1zM2 4.2v.4l6 4 6-4v-.4z"/></svg>
          daniel@kestrovaelectric.com
        </li>
        <li>
          <svg viewBox="0 0 16 16" aria-hidden="true"><path d="M8 1a7 7 0 100 14A7 7 0 008 1zm0 1.5c.8 0 1.7 1.6 2 4H6c.3-2.4 1.2-4 2-4zM6 8h4c-.1 2.7-1.1 5.5-2 5.5S6.1 10.7 6 8zM2.6 7h2c0-1.5.3-2.9.8-3.9A5.5 5.5 0 002.6 7zm8.8 0h2a5.5 5.5 0 00-2.8-3.9c.5 1 .8 2.4.8 3.9z"/></svg>
          www.kestrovaelectric.com
        </li>
      </ul>
      <address class="address">
        418 Calder Street NW<br>
        Suite 210, Brookfield<br>
        MI 49612
      </address>
    </div>

    <div class="partner-badge" role="img" aria-label="Tarrow Alliance partner badge">
      <span></span>
    </div>
  </section>

</body>
</html>
```